Business Card & Email Signature Design || Upmarket + Luxury

Rima Vale Honey, a New Zealand Manuka Honey company needs a Business Card & Email Signature design.

Our logo's are attached in Gold & Black versions, feel free to be creative with how you use the logo and it's patterns in your design.

Style:
- Looking for an Elegant, Luxurious, Upmarket feel.
- Black/Matte Black Card, Gold Foil, UV Embossing

Information to Add:

- Logo
- Company Name: Rima Vale Honey
- Name: Martin Delrow
- Title: Creative Director
- Phone: +64 2815 90 617
- Email: martin@rimavalehoney.example.nz
- Website: www.rimavalehoney.example.nz

- Socials: ***For email Signature Only***
- Facebook: https://www.facebook.com/rimavalehoney/
- Instagram: https://www.instagram.com/rimavalehoney/

Target Market(s)

Asia/Europe Luxury, Upmarket

Contact Information for Business Card

- Logo
- Name: Martin Delrow
- Phone: +64 2815 90 617

Font styles to use
Other font styles liked:
• Champagne & Limousines (Attached)

Requirements
Must have
• Business Card & Email Signature Design.

Looking for a Sleek, Luxury, Upmarket Design.

```html
<!DOCTYPE html>
<html lang="en">
<head>
<meta charset="utf-8">
<title>Rima Vale Honey – Business Card &amp; Email Signature</title>
<link rel="stylesheet" href="https://fonts.googleapis.com/css2?family=Josefin+Sans:wght@400&family=Lato:wght@400;700;900&display=swap">
<style>
  :root {
    --backdrop: #444444;
    --card-black: #0d0d0d;
    --card-black-soft: #1a1a1a;
    --gold: #d2ac64;
    --gold-light: #f0df95;
    --gold-deep: #c79f5f;
    --paper: #ffffff;
    --ink: #333333;
    --bar-black: #151515;
    --soft-white: #e8e8e8;
  }
  * { margin: 0; padding: 0; box-sizing: border-box; }
  html, body { width: 1200px; height: 1133px; overflow: hidden; background: var(--backdrop); }
  .canvas { position: relative; width: 1200px; height: 1133px; }

  .card {
    position: absolute; top: 304px; height: 231px;
    background: radial-gradient(ellipse at 40% 20%, var(--card-black-soft), var(--card-black) 70%);
    overflow: hidden;
  }
  .card--front { left: 164px; width: 390px; }
  .card--back { left: 595px; width: 386px; }

  .brand-mark { position: absolute; border: 1.5px solid var(--gold); border-radius: 50%; }
  .brand-name {
    position: absolute; white-space: nowrap; text-align: center;
    font-family: "Josefin Sans", sans-serif; font-weight: 400; color: var(--gold);
    text-transform: uppercase;
  }

  .card--front .brand-mark { left: 77px; top: 64px; width: 50px; height: 50px; }
  .card--front .brand-name { left: 10px; width: 184px; top: 124px; font-size: 13.5px; letter-spacing: 1.6px; }
  .card-divider { position: absolute; left: 195px; top: 67px; width: 1px; height: 71px; background: #555; }
  .card-person { position: absolute; left: 212px; top: 66px; font-family: Lato, sans-serif; }
  .card-person__name { color: var(--gold-light); font-weight: 900; font-size: 15px; letter-spacing: 0.6px; text-transform: uppercase; }
  .card-person__title { color: var(--soft-white); font-size: 10.5px; margin-top: 1px; }
  .card-contact { position: absolute; left: 210px; top: 115px; font-family: Lato, sans-serif; color: var(--soft-white); font-size: 10px; line-height: 14px; }
  .card-contact li { list-style: none; display: flex; align-items: center; gap: 4px; }
  .card-contact svg { width: 11px; height: 11px; flex: none; }
  .card-band {
    position: absolute; left: 0; bottom: 0; width: 100%; height: 34px;
    background: linear-gradient(110deg, var(--gold-deep) 35%, var(--gold-light) 50%, var(--gold-deep) 62%);
    font-family: Lato, sans-serif; font-size: 11px; color: #111; text-align: center; line-height: 34px;
  }

  .card--back .brand-mark { left: 147px; top: 47px; width: 92px; height: 92px; }
  .card--back .brand-name { left: 0; width: 386px; top: 144px; font-size: 21px; letter-spacing: 2.4px; }

  .signature { position: absolute; left: 159px; top: 630px; width: 822px; height: 247px; background: var(--paper); overflow: hidden; }
  .signature-person { position: absolute; left: 57px; top: 22px; font-family: Lato, sans-serif; }
  .signature-person__name { color: var(--gold); font-weight: 700; font-size: 30px; line-height: 34px; }
  .signature-person__title { color: var(--ink); font-size: 20px; line-height: 24px; }
  .signature-contact { position: absolute; left: 57px; top: 99px; font-family: Lato, sans-serif; font-size: 20px; color: #444; line-height: 25px; }
  .signature-contact li { list-style: none; display: flex; align-items: center; gap: 10px; }
  .signature-contact svg { width: 22px; height: 22px; flex: none; }
  .signature .brand-mark { left: 570px; top: 24px; width: 100px; height: 100px; border-width: 2px; }
  .signature .brand-name { left: 480px; width: 280px; top: 131px; font-size: 24px; letter-spacing: 2.4px; }
  .signature-rule { position: absolute; left: 0; top: 203px; width: 100%; height: 3px; background: var(--gold); }
  .signature-bar {
    position: absolute; left: 0; top: 206px; width: 100%; height: 41px; background: var(--bar-black);
    display: flex; align-items: center; justify-content: center; gap: 8px;
    font-family: Lato, sans-serif; font-size: 20px; color: var(--gold);
  }
  .social-dot { width: 27px; height: 27px; border-radius: 50%; background: var(--gold-light); display: inline-block; }
  .social-sep { color: #888; margin: 0 2px; }
</style>
</head>
<body>
<div class="canvas">
  <svg width="0" height="0" style="position:absolute" aria-hidden="true">
    <defs>
      <symbol id="icon-phone" viewBox="0 0 24 24"><path d="M6.5 3l3 4-2 2c1 2.5 3 4.5 5.5 5.5l2-2 4 3-2 3.5C11 19 5 13 3 6.5z" fill="none" stroke="currentColor" stroke-width="1.8" stroke-linejoin="round"/></symbol>
      <symbol id="icon-mail" viewBox="0 0 24 24"><path d="M2 5h20v14H2z M2 5l10 8 10-8" fill="none" stroke="currentColor" stroke-width="1.8" stroke-linejoin="round"/></symbol>
      <symbol id="icon-globe" viewBox="0 0 24 24"><g fill="none" stroke="currentColor" stroke-width="1.5"><circle cx="12" cy="12" r="10"/><ellipse cx="12" cy="12" rx="4.5" ry="10"/><path d="M2 12h20M4 7h16M4 17h16"/></g></symbol>
    </defs>
  </svg>

  <section class="card card--front">
    <span class="brand-mark" aria-hidden="true"></span>
    <div class="brand-name">Rima Vale Honey</div>
    <span class="card-divider"></span>
    <div class="card-person">
      <div class="card-person__name">Martin Delrow</div>
      <div class="card-person__title">Creative Director</div>
    </div>
    <ul class="card-contact">
      <li><svg style="color:var(--gold)"><use href="#icon-phone"/></svg>+64 2815 90 617</li>
      <li><svg style="color:var(--gold)"><use href="#icon-mail"/></svg>martin@rimavalehoney.example.nz</li>
    </ul>
    <div class="card-band">www.rimavalehoney.example.nz</div>
  </section>

  <section class="card card--back">
    <span class="brand-mark" aria-hidden="true"></span>
    <div class="brand-name">Rima Vale Honey</div>
  </section>

  <section class="signature">
    <div class="signature-person">
      <div class="signature-person__name">Martin Delrow</div>
      <div class="signature-person__title">Creative Director</div>
    </div>
    <ul class="signature-contact">
      <li><svg style="color:var(--gold)"><use href="#icon-phone"/></svg>+64 2815 90 617</li>
      <li><svg style="color:var(--gold)"><use href="#icon-mail"/></svg>martin@rimavalehoney.example.nz</li>
      <li><svg style="color:var(--gold)"><use href="#icon-globe"/></svg>www.rimavalehoney.example.nz</li>
    </ul>
    <span class="brand-mark" aria-hidden="true"></span>
    <div class="brand-name">Rima Vale Honey</div>
    <span class="signature-rule"></span>
    <div class="signature-bar">
      <span>Follow us on:</span>
      <span class="social-dot" role="img" aria-label="First social profile link"></span>
      <span class="social-dot" role="img" aria-label="Second social profile link"></span>
      <span class="social-sep">/</span>
      <span>rimavalehoney</span>
    </div>
  </section>
</div>
</body>
</html>
```